Personal Finance Author needs a postcard

Hi there,

I am a Canadian personal finance author and have published a new book called The Wealth Compass.

I teach Millennials how to create a 6-figure portfolio through investing (https://www.dariafelt.com/)

I'm speaking at some conferences so we were going to print some postcards to hand out to attendees with our info and calls-to-action on them.

I am looking for 4x6 (horizontal) postcard (no space needed for shipping label).

Logos, Headshots and Book Cover:
https://files.cloudvaultex.com/folders/8kQpZrT2mWvN4xLbJ7sHdYc3FgA9eUoRi?usp=sharing

Both sides will be full colour. I would like a clean and simple look. Our main sites are www.DariaFelt.com and www.TheWealthCompassBook.com if you want to get a sense of style and design.
I also uploaded a few marketing materials so you can see the existing designs.

Side 1:
Get Instant Access to your Free Resources - main headline

(small bullets underneath)
- The Wealth Compass Checklist
- Financial Worksheets
- Database of Investment Tools

DariaFelt.com/Resources

At the bottom, include "Don't forget to follow Daria Felt on social media:
Linkedin: @dariafelt7
Facebook: @thewealthcompassbook Instagram: @thewealthcompassbook Twitter: @WealthCompassBk"

Side 2:
Headline - Want to work directly with Daria and The Wealth Compass team to help you make your money grow and stay safe?

Work with us to (bullet point list)...
- Hire Daria as a Keynote Speaker
- Teach Financial Literacy Workshops
- Receive Financial Coaching

Want To Learn More About How We Can Help?
DariaFelt.com/Services

Include my contact info:
Daria Felt
Author | Speaker | Investor
daria@thewealthcompassbook.com
416-555-0187

Target Market(s)

Millennials who want to learn how to save and invest their money. I focus on stock market investing, real estate investing and entrepreneurship.

Industry/Entity Type

Financial Service

Font styles to use
Sans Serif

Colors

Designer to choose colors to be used in the design.

Requirements
Must have
• Photo of Daria Felt
• The Wealth Compass logo
• Green, Gold/Yellow to match existing colours
• modern business style postcard

```html
<!DOCTYPE html>
<html lang="en">
<head>
<meta charset="UTF-8">
<title>The Wealth Compass – Postcard</title>
<link href="https://fonts.googleapis.com/css2?family=Bebas+Neue&family=Montserrat:wght@500;600;700;800;900&family=Open+Sans:ital,wght@0,400;0,600;1,700;1,800&display=swap" rel="stylesheet">
<style>
  :root {
    --gold: #e9b52b;
    --gold-deep: #d79f22;
    --green: #3a6d3d;
    --green-dark: #315a34;
    --green-light: #45803f;
    --ink: #111111;
    --white: #ffffff;
    --mist: #d9d9d9;
    --backdrop: #b4b4b4;
  }
  * { box-sizing: border-box; margin: 0; padding: 0; }
  html, body { width: 1200px; height: 1200px; overflow: hidden; }
  body { background: var(--backdrop); position: relative; font-family: "Montserrat", sans-serif; }

  .postcard {
    position: absolute; left: 210px; width: 780px; height: 520px;
    overflow: hidden; box-shadow: 0 6px 18px rgba(0,0,0,.25);
  }
  .postcard--front { top: 60px; background: linear-gradient(160deg, var(--gold), var(--gold-deep)); }
  .postcard--back { top: 620px; background: var(--green-light); }
  .shapes { position: absolute; inset: 0; width: 100%; height: 100%; }

  /* Front */
  .portrait {
    position: absolute; left: 14px; top: 8px; width: 320px; height: 512px;
    background: linear-gradient(180deg, #5a3d2c 0%, #d8ab8a 22%, #f2efe9 42%, #1e1f24 60%, #17181c 100%);
    border-radius: 120px 120px 0 0;
  }
  .headline {
    position: absolute; left: 360px; top: 92px;
    font-family: "Bebas Neue", sans-serif; font-weight: 400; font-size: 52px; line-height: .95;
    color: var(--ink); letter-spacing: -1px; word-spacing: -4px;
    white-space: nowrap; transform: scaleX(.92); transform-origin: left top;
  }
  .headline span { display: block; }
  .resource-list {
    position: absolute; left: 360px; top: 214px; list-style: none;
    font-weight: 700; font-size: 20px; line-height: 1.45; color: var(--ink);
  }
  .resource-list li::before {
    content: ""; display: inline-block; width: 9px; height: 9px; border-radius: 50%;
    background: var(--green); margin-right: 9px; vertical-align: 4px;
  }
  .social-list {
    position: absolute; left: 388px; top: 368px; list-style: none;
    color: var(--white); font-size: 14px; font-weight: 600; line-height: 1.75;
  }
  .social-list li { display: flex; align-items: center; gap: 10px; }
  .social-dot { width: 13px; height: 13px; border: 1.6px solid var(--white); border-radius: 50%; }
  .social-dot--none { border-color: transparent; }
  .resource-url {
    position: absolute; left: 408px; top: 474px;
    font-family: "Open Sans", sans-serif; font-size: 18px; color: var(--white);
  }

  /* Back */
  .offer-heading {
    position: absolute; left: 40px; top: 22px; width: 560px;
    font-family: "Open Sans", sans-serif; font-style: italic; font-weight: 800;
    font-size: 21px; line-height: 1.12; color: var(--gold);
  }
  .offer-list {
    position: absolute; left: 46px; top: 128px; list-style: none;
    font-family: "Open Sans", sans-serif; font-style: italic; font-weight: 700;
    font-size: 13px; line-height: 1.4; color: var(--gold);
  }
  .offer-list li::before {
    content: ""; display: inline-block; width: 7px; height: 7px; border-radius: 50%;
    background: var(--gold); margin-right: 10px; vertical-align: 2px;
  }
  .help-prompt {
    position: absolute; left: 40px; top: 300px;
    font-family: "Open Sans", sans-serif; font-style: italic; font-weight: 800;
    font-size: 32px; line-height: 1.05; letter-spacing: -.5px; text-transform: uppercase;
    white-space: nowrap;
  }
  .help-prompt span { display: block; }
  .help-prompt .tone-1 { color: var(--white); }
  .help-prompt .tone-2 { color: #ececec; }
  .help-prompt .tone-3 { color: var(--mist); }
  .contact {
    position: absolute; left: 470px; top: 350px; color: var(--ink);
  }
  .contact-name { font-weight: 900; font-size: 26px; letter-spacing: 1px; text-align: center; }
  .contact-role { font-weight: 600; font-size: 9.5px; text-align: center; }
  .contact-email { font-weight: 700; font-size: 10px; text-align: center; }
  .contact-phone {
    position: absolute; left: 390px; top: 420px; display: flex; align-items: center; gap: 14px;
    font-family: "Open Sans", sans-serif; font-style: italic; font-weight: 800;
    font-size: 34px; color: var(--ink); white-space: nowrap;
  }
  .phone-icon { width: 54px; height: 36px; }
</style>
</head>
<body>

<section class="postcard postcard--front">
  <svg class="shapes" viewBox="0 0 780 520" aria-hidden="true">
    <polygon points="0,0 340,0 400,60 0,60" fill="var(--green-dark)"/>
    <polygon points="0,400 0,520 110,520" fill="var(--green)"/>
    <path d="M320,348 L575,356 Q612,360 640,392 L760,520 L320,520 Z" fill="var(--green)"/>
  </svg>
  <div class="portrait" role="img" aria-label="Portrait photo of Daria Felt in a dark blazer, hand on hip, smiling"></div>

  <h1 class="headline"><span>Get Instant Access</span><span>To Your Free Resources</span></h1>
  <ul class="resource-list">
    <li>The Wealth Compass Checklist</li>
    <li>Financial Worksheets</li>
    <li>Database of Investment Tools</li>
  </ul>
  <ul class="social-list">
    <li><span class="social-dot social-dot--none"></span>@dariafelt7</li>
    <li><span class="social-dot"></span>@thewealthcompassbook</li>
    <li><span class="social-dot"></span>@thewealthcompassbook</li>
    <li><span class="social-dot"></span>@WealthCompassBk</li>
  </ul>
  <p class="resource-url">DariaFelt.com/Resources</p>
</section>

<section class="postcard postcard--back">
  <svg class="shapes" viewBox="0 0 780 520" aria-hidden="true">
    <rect x="0" y="0" width="780" height="230" fill="var(--green-dark)"/>
    <path d="M430,230 Q600,210 780,100 L780,230 Z" fill="var(--green)"/>
    <path d="M330,230 L780,230 L780,520 L440,520 Q400,440 330,230 Z" fill="var(--gold)"/>
  </svg>

  <h2 class="offer-heading">Want to work directly with Daria and The Wealth Compass Team to help you make your money grow and stay safe?</h2>
  <ul class="offer-list">
    <li>Hire Daria as a Keynote Speaker</li>
    <li>Teach Financial Literacy Workshops</li>
    <li>Receive Financial Coaching</li>
  </ul>

  <p class="help-prompt">
    <span class="tone-1">Want To Learn</span>
    <span class="tone-2">More About</span>
    <span class="tone-3">How We Can Help?</span>
  </p>

  <div class="contact">
    <p class="contact-name">Daria Felt</p>
    <p class="contact-role">Author | Speaker | Investor</p>
    <p class="contact-email">daria@thewealthcompassbook.com</p>
  </div>
  <div class="contact-phone">
    <svg class="phone-icon" viewBox="0 0 54 36" aria-hidden="true">
      <rect x="2" y="2" width="50" height="32" rx="8" fill="none" stroke="var(--ink)" stroke-width="3"/>
      <path d="M19,10 Q17,12 19,17 Q23,24 30,27 Q34,28 36,25 L33,21 L29,23 Q25,20 23,16 L25,13 Z" fill="none" stroke="var(--ink)" stroke-width="2.4" stroke-linejoin="round"/>
    </svg>
    <span>416-555-0187</span>
  </div>
</section>

</body>
</html>
```